Detox Poster Design Project

I am a naturopath that works in Melbourne. I require a poster that I can put up in my natural therapies clinic that is advertising a detox program that I am offering. The program runs for 3 or 6 weeks and is designed to help your liver, gut and kidney cleanse toxins more efficiently, leaving you feeling energised and healthy.

I would like to see designs that are fresh, organic, clear and contemporary to look at. I want to sell the idea of feeling good, wellbeing and vitality to the potential client. Colours I like include greens, greys and blues.

The final design should communicate health and happiness.

• Please include the photo of the woman in nature.Poster size will be A2 594mm by 420mm
• I have attached the design work for my business cards that you can use. It would be great if the colours and style are in keeping with the existing design work for my business. I have also attached an extra image (almond milk photo) just in case you could see a use for it.

Many thanks.
• No hippy, new age looking design.

```html
<!DOCTYPE html>
<html lang="en">
<head>
<meta charset="utf-8">
<title>It's Sensible Detox Time</title>
<link rel="stylesheet" href="https://fonts.googleapis.com/css2?family=Cormorant+Garamond:ital,wght@1,300;1,400&display=swap">
<style>
  :root {
    --haze: #e6edc4;
    --leaf-light: #b9cd80;
    --leaf-mid: #6f9a4c;
    --leaf-deep: #2f5a2c;
    --forest-dark: #173220;
    --skin-warm: rgba(214, 186, 150, 0.75);
    --top-pale: rgba(222, 228, 220, 0.8);
    --text-light: #ffffff;
  }
  html, body {
    margin: 0;
    padding: 0;
    overflow: hidden;
    background: #ffffff;
  }
  .poster {
    position: relative;
    width: 849px;
    height: 1200px;
    overflow: hidden;
    font-family: "Cormorant Garamond", Georgia, serif;
    color: var(--text-light);
  }
  .poster__photo {
    position: absolute;
    inset: 0;
    background:
      radial-gradient(ellipse 13% 9% at 50% 90%, var(--top-pale), rgba(222,228,220,0) 75%),
      radial-gradient(ellipse 12% 14% at 50% 70%, var(--skin-warm), rgba(214,186,150,0) 75%),
      radial-gradient(ellipse 9% 20% at 24% 52%, rgba(214,186,150,0.45), rgba(214,186,150,0) 75%),
      radial-gradient(ellipse 9% 20% at 76% 52%, rgba(214,186,150,0.45), rgba(214,186,150,0) 75%),
      radial-gradient(ellipse 18% 12% at 12% 88%, rgba(120,165,70,0.7), rgba(120,165,70,0) 75%),
      radial-gradient(ellipse 16% 12% at 85% 85%, rgba(150,180,80,0.55), rgba(150,180,80,0) 75%),
      radial-gradient(ellipse 30% 20% at 15% 95%, rgba(20,45,26,0.9), rgba(20,45,26,0) 75%),
      radial-gradient(ellipse 30% 22% at 90% 70%, rgba(28,58,34,0.8), rgba(28,58,34,0) 75%),
      radial-gradient(ellipse 25% 18% at 8% 62%, rgba(40,80,40,0.7), rgba(40,80,40,0) 75%),
      radial-gradient(ellipse 60% 30% at 50% 12%, rgba(244,247,220,0.95), rgba(244,247,220,0) 70%),
      linear-gradient(180deg, var(--haze) 0%, var(--leaf-light) 28%, var(--leaf-mid) 55%, var(--leaf-deep) 80%, var(--forest-dark) 100%);
  }
  .headline {
    position: absolute;
    left: 0;
    right: 0;
    top: 118px;
    margin: 0;
    text-align: center;
    font-weight: 400;
    font-style: italic;
    font-size: 124px;
    line-height: 125px;
    letter-spacing: 8px;
  }
  .intro {
    position: absolute;
    left: 0;
    right: 0;
    top: 466px;
    margin: 0;
    text-align: center;
    font-style: italic;
    font-weight: 400;
    font-size: 24px;
    line-height: 37px;
    letter-spacing: 2px;
  }
  .intro__closing {
    display: block;
    line-height: 27px;
    margin-top: 0;
  }
  .contact {
    position: absolute;
    left: 99px;
    width: 651px;
    top: 1066px;
    height: 72px;
  }
  .contact__brace {
    position: absolute;
    top: 0;
    width: 16px;
    height: 72px;
  }
  .contact__brace--left { left: 0; }
  .contact__brace--right { right: 0; }
  .contact__text {
    margin: 0;
    padding-top: 8px;
    padding-left: 28px;
    font-style: italic;
    font-size: 21px;
    line-height: 28px;
    letter-spacing: 1.6px;
    white-space: nowrap;
  }
</style>
</head>
<body>
<main class="poster">
  <div class="poster__photo" role="img" aria-label="Photo of a woman seen from behind with arms raised, standing in lush green tropical forest"></div>

  <h1 class="headline">It’s Sensible<br>Detox Time</h1>

  <p class="intro">
    Overindulged over the holidays?<br>
    Have a detox program tailored for you.<br>
    <span class="intro__closing">Press reset on your bad eating habits to<br>feel energised and vital</span>
  </p>

  <div class="contact">
    <svg class="contact__brace contact__brace--left" viewBox="0 0 16 72" aria-hidden="true">
      <path d="M14 1 C6 1 8 12 8 24 C8 32 6 35 1 36 C6 37 8 40 8 48 C8 60 6 71 14 71" fill="none" stroke="#ffffff" stroke-width="1.4"/>
    </svg>
    <p class="contact__text">
      For more information contact Clara Whitfield on 0400 123 456<br>
      email: info@greenleafnaturopathy.com
    </p>
    <svg class="contact__brace contact__brace--right" viewBox="0 0 16 72" aria-hidden="true">
      <path d="M2 1 C10 1 8 12 8 24 C8 32 10 35 15 36 C10 37 8 40 8 48 C8 60 10 71 2 71" fill="none" stroke="#ffffff" stroke-width="1.4"/>
    </svg>
  </div>
</main>
</body>
</html>
```